This book will apply the 12 Steps to gaming addiction, also known as video game addiction. The primary purpose of the book is to provide an effective solution for this new type of addiction. The solution is based on the rich and successful concepts of traditional twelve-step programs like RL.

The title on the cover will be "Nine Doors Past the Glowing Screen" and "by Martin Quorby". A subtitle can be used if it works in your design of "A Practical Path Beyond Compulsive Console Play". Cover will be for a 6" x 9" book approximately 110 pages in length.

Some back cover text including some review quotes and an author bio are in the attached Word doc. There is also an author photo attached for for the back cover.

Requirements
Must have
• For the cover design it could be stylized, or an image, a partial image, or whatever. I am open to suggestions. Think about what would be noticed by a person searching for help with moderating their video game use, or by the parents or loved ones of problem gamers. Something contemporary and eye catching.

```html
<!DOCTYPE html>
<html lang="en">
<head>
<meta charset="utf-8">
<title>Nine Doors Past the Glowing Screen — Cover Wrap</title>
<link href="https://fonts.googleapis.com/css2?family=Montserrat:wght@500;700;800&family=Open+Sans:wght@400;600;700&display=swap" rel="stylesheet">
<style>
  :root{
    --stage:#e6e6e8;
    --paper:#ffffff;
    --paper-tint:#ece8f1;
    --blue:#1c7fc4;
    --blue-deep:#1565a6;
    --ink:#2b2b2f;
    --grey:#8a8a90;
    --wave-pink:#e9b9d2;
    --wave-blue:#b9d3ec;
    --steel:#7c7e86;
  }
  *{box-sizing:border-box;margin:0;padding:0}
  html,body{width:848px;height:1200px;overflow:hidden}
  body{background:var(--stage);font-family:"Open Sans",Arial,sans-serif;color:var(--ink);position:relative}

  .wrap{
    position:absolute;left:24px;top:312px;width:800px;height:576px;
    display:flex;box-shadow:0 8px 24px rgba(0,0,0,.18);
    background:linear-gradient(180deg,var(--paper) 0%,var(--paper) 45%,var(--paper-tint) 100%);
  }

  /* back cover */
  .back{width:384px;height:100%;padding:20px 22px 14px;position:relative;overflow:hidden}
  .back__wave{position:absolute;left:0;right:0;top:300px;height:200px;
    background:radial-gradient(ellipse at 40% 50%,rgba(233,185,210,.35),rgba(185,211,236,.2) 55%,transparent 75%)}
  .praise{position:relative;text-align:center}
  .praise__label{font-family:"Montserrat",sans-serif;font-weight:700;color:var(--blue);font-size:9.5px;letter-spacing:.3px}
  .praise__title{font-family:"Montserrat",sans-serif;font-weight:800;color:var(--blue);font-size:9.5px;margin-bottom:8px}
  .quote{font-size:6.6px;line-height:1.4;margin-bottom:8px}
  .quote__by{display:block;font-weight:700}
  .rule{position:relative;height:1px;background:#555;margin:4px 0 10px}
  .blurb{position:relative;font-size:6.6px;line-height:1.42;margin-bottom:8px;text-align:justify}
  .blurb strong{font-weight:700}
  .bio{position:relative;display:flex;gap:9px;margin-top:10px}
  .bio__photo{flex:0 0 52px;height:62px;background:linear-gradient(160deg,#c9b8a4,#8d7a6a);}
  .bio__text{font-size:6.6px;line-height:1.42;text-align:justify}

  /* spine */
  .spine{width:32px;height:100%;position:relative;
    background:linear-gradient(90deg,#f2f2f4,#ffffff 50%,#f2f2f4);}
  .spine__line{position:absolute;left:50%;top:14px;transform-origin:0 0;transform:rotate(90deg) translateY(-50%);
    white-space:nowrap;font-family:"Montserrat",sans-serif;font-weight:800;font-size:10.5px;letter-spacing:.3px}
  .spine__author{color:var(--grey);margin-right:14px}
  .spine__title{color:var(--blue)}

  /* front cover */
  .front{width:384px;height:100%;position:relative;overflow:hidden;text-align:center}
  .front__author{position:absolute;top:26px;left:0;right:0;font-family:"Montserrat",sans-serif;font-weight:700;
    color:var(--grey);font-size:12px;letter-spacing:.4px}
  .title{position:absolute;top:88px;left:0;right:0;font-family:"Montserrat",sans-serif;color:var(--blue);line-height:.95}
  .title__small{display:block;font-weight:700;font-size:21px}
  .title__big{display:block;font-weight:800;font-size:46px;letter-spacing:-.5px}
  .title__mid{display:block;font-weight:800;font-size:30px;margin-top:4px}
  .front__art{position:absolute;left:0;right:0;top:250px;bottom:0;
    background:
      radial-gradient(ellipse 70% 40% at 50% 75%,rgba(110,112,120,.85),rgba(150,152,160,.4) 60%,transparent 80%),
      linear-gradient(180deg,rgba(185,211,236,.45) 0%,rgba(233,185,210,.45) 35%,rgba(236,232,241,.4) 55%,#c9cad0 100%);}
</style>
</head>
<body>
  <main class="wrap">
    <section class="back">
      <div class="back__wave" role="img" aria-label="Faint pink and blue particle wave"></div>
      <div class="praise">
        <p class="praise__label">PRAISE FOR</p>
        <p class="praise__title">NINE DOORS PAST THE GLOWING SCREEN</p>
        <p class="quote">“A must-read for anyone who is addicted to or thinks they may have a problem with digital gaming. This eloquent work will also be useful to academics and clinicians exploring potential solutions. The author recognizes the similarities between gaming addiction and other addictions, and logically applies one of the most effective known solutions for addiction - The Twelve Steps.”<span class="quote__by">- Dale Brennick, Noted Interventionist and Keynote Speaker -</span></p>
        <p class="quote">“If you suffer from digital gaming addiction, I strongly encourage you to use this book as your road map to get you back to the real world.”<span class="quote__by">- Owen Calloway, Founder of Signal Street Review -</span></p>
        <p class="quote">“As a high school teacher for 24 years, husband, father, coach, and 12-Step member, I can assure you that this book will transform the life of anyone who is addicted to video games. Well written, easy to understand, and a wonderful book that will provide you with a clear road map to recovery, and this includes teenagers, a group I have been working with in the classroom for decades.”<span class="quote__by">- Theo Ramsell, Harbor Vale, OR High School Teacher -</span></p>
      </div>
      <div class="rule"></div>
      <p class="blurb"><strong>A Practical Path Beyond Compulsive Console Play — an effective solution to the challenge of Digital Gaming Addiction based on the rich and successful tradition of the Twelve Steps.</strong></p>
      <p class="blurb"><strong>Addiction to Digital Gaming is a new and troubling phenomenon that has burst upon an unprepared society with alarming speed.</strong> Many people crave the use of Digital Games in a strikingly similar way to any other addict. Digital Games are a complex software and hardware system that have been designed to promote continued and progressive usage. This sophisticated technology clearly feeds on natural addictive tendencies.</p>
      <p class="blurb"><strong>The 12 Steps are one of the most effective methods for treating addiction in human history.</strong> Originating with Recovery League in 1939, the 12 Steps have since been used to treat a variety of other addictions, including drugs, sex, gambling, eating disorders, and many others. Now in this groundbreaking work the 12 Steps are applied to the complex and evolving contemporary phenomenon of Digital Gaming Addiction.</p>
      <div class="bio">
        <div class="bio__photo" role="img" aria-label="Author portrait photograph"></div>
        <p class="bio__text">Martin Quorby is a Technology Consultant and Writer with many years of professional coding and consulting experience. He also struggled with addiction to drugs and alcohol and is now clean and sober in a Twelve-Step program for over 17 years. This unique combination of 12-Step experience and technology expertise led him to create Nine Doors Past the Glowing Screen.</p>
      </div>
    </section>

    <section class="spine">
      <p class="spine__line"><span class="spine__author">MARTIN QUORBY</span><span class="spine__title">NINE DOORS PAST THE GLOWING SCREEN</span></p>
    </section>

    <section class="front">
      <div class="front__art" role="img" aria-label="Pink and blue particle wave above a close-up of a grey game controller"></div>
      <p class="front__author">MARTIN QUORBY</p>
      <h1 class="title">
        <span class="title__big">Nine Doors</span>
        <span class="title__small">Past the</span>
        <span class="title__mid">GLOWING SCREEN</span>
      </h1>
    </section>
  </main>
</body>
</html>
```